Business Card Design

My business is writing crime novels to entertain readers. I write legal thrillers and mysteries. I need a card for publishers, agents, other authors, and media.

Industry/Entity Type

Legal

Contact Information for Business Card

Paul Trenholt
www.trenholtnoir.example
pbtrenholt@mailbox.example
0064 27 5170942

```html
<!DOCTYPE html>
<html lang="en">
<head>
<meta charset="utf-8">
<title>Paul Trenholt — Author</title>
<link rel="stylesheet" href="https://fonts.googleapis.com/css2?family=Arimo:wght@400;700&display=swap">
<style>
  :root {
    --ink: #151515;
    --paper: #ffffff;
    --accent: #d8532a;
    --text: #111111;
    --photo-light: #9a9a9a;
    --photo-mid: #6e6e6e;
    --photo-dark: #1c1c1c;
  }
  * { margin: 0; padding: 0; box-sizing: border-box; }
  html, body {
    width: 1200px;
    height: 741px;
    overflow: hidden;
    background: var(--paper);
  }
  .card {
    position: relative;
    width: 1200px;
    height: 741px;
    background: var(--paper);
    font-family: "Arimo", Arial, sans-serif;
    color: var(--text);
  }
  .dark-band {
    position: absolute;
    left: 0;
    top: 0;
    width: 1200px;
    height: 534px;
    background: var(--ink);
  }
  .portrait {
    position: absolute;
    left: 71px;
    top: 0;
    width: 426px;
    height: 646px;
    background:
      linear-gradient(180deg, transparent 45%, rgba(20,20,20,0.85) 100%),
      radial-gradient(ellipse at 50% 30%, var(--photo-light) 0%, var(--photo-mid) 70%);
  }
  .identity {
    position: absolute;
    left: 556px;
    top: 447px;
    width: 404px;
    text-align: right;
  }
  .identity__name {
    display: block;
    text-align: left;
    font-weight: 400;
    font-size: 54px;
    line-height: 1;
    letter-spacing: 0.5px;
    color: var(--accent);
    text-transform: uppercase;
    white-space: nowrap;
  }
  .identity__role {
    display: block;
    margin-top: 7px;
    font-weight: 700;
    font-size: 17px;
    letter-spacing: 0.8px;
    color: var(--paper);
  }
  .contact {
    position: absolute;
    left: 557px;
    top: 545px;
    list-style: none;
  }
  .contact__item {
    font-size: 24.5px;
    line-height: 31px;
    white-space: nowrap;
  }
  .contact__item--web {
    margin-top: 4px;
    font-weight: 700;
    font-size: 28px;
    letter-spacing: 1.6px;
  }
</style>
</head>
<body>
  <main class="card">
    <div class="dark-band"></div>
    <div class="portrait" role="img" aria-label="Portrait photograph of the author in a dark leather jacket and white shirt"></div>
    <div class="identity">
      <h1 class="identity__name">Paul Trenholt</h1>
      <span class="identity__role">AUTHOR</span>
    </div>
    <ul class="contact">
      <li class="contact__item">0064 27 5170942</li>
      <li class="contact__item">pbtrenholt@mailbox.example</li>
      <li class="contact__item contact__item--web">www.trenholtnoir.example</li>
    </ul>
  </main>
</body>
</html>
```